Bright Path Therapies business cards and stationary

Need business cards and stationary designed to match previously made logo for for a new company based in Sydney NSW called 'Bright Path Therapies'.

We provide early intervention services and diagnostic assessment for children with disability and their families. I would like designs that are colourful and child friendly - possibly using feet/footprints/steps on a white background. The final design should communicate that we are family friendly, accepting and fun to work with.

Target Market(s)

Parents and Families
Teachers
Allied Health Professionals

Industry/Entity Type

Psychology

Contact Information for Business Card

Bright Path Therapies
www.brightpaththerapies.example
info@brightpaththerapies.example

Font styles to use
Sans Serif
Decorative
Script

Requirements
Must have
• Match the font and colour scheme of logo, along with footprint picture
Nice to have
• Clean and simple, while reflecting that I am working with families.
• Also- editable for when we make staff specific cards.

```html
<!DOCTYPE html>
<html lang="en">
<head>
<meta charset="utf-8">
<title>Bright Path Therapies – Business Cards</title>
<link rel="stylesheet" href="https://fonts.googleapis.com/css2?family=Montserrat:wght@400;500;600&family=Amatic+SC:wght@700&display=swap">
<style>
  :root {
    --stage: #111111;
    --card: #ffffff;
    --brand-red: #e8433a;
    --brand-blue: #2b56a8;
    --brand-orange: #f4a236;
    --brand-sky: #1f76c2;
    --ink: #3a3a3a;
  }
  * { margin: 0; padding: 0; box-sizing: border-box; }
  html, body {
    width: 1200px;
    height: 1000px;
    overflow: hidden;
    background: var(--stage);
  }
  .stage {
    position: relative;
    width: 1200px;
    height: 1000px;
  }
  .card {
    position: absolute;
    width: 500px;
    height: 290px;
    background: var(--card);
    border-radius: 22px;
  }
  .card--front { left: 70px; top: 355px; }
  .card--back { left: 630px; top: 355px; }

  .footprint {
    position: absolute;
    border-radius: 48% 52% 46% 54% / 60% 60% 40% 40%;
  }
  .footprint--blue {
    left: 40px; top: 34px;
    width: 78px; height: 104px;
    background: var(--brand-blue);
    transform: rotate(-12deg);
  }
  .footprint--orange {
    left: 62px; top: 148px;
    width: 78px; height: 104px;
    background: var(--brand-orange);
    transform: rotate(14deg);
  }

  .brand {
    display: flex;
    align-items: center;
    gap: 10px;
  }
  .brand__dot {
    flex: none;
    border-radius: 50%;
    background: var(--brand-red);
  }
  .brand__name {
    font-family: "Montserrat", sans-serif;
    font-weight: 600;
    color: var(--brand-sky);
    letter-spacing: 0.02em;
  }

  .card--front .brand {
    position: absolute;
    right: 34px; top: 46px;
  }
  .card--front .brand__dot { width: 40px; height: 40px; }
  .card--front .brand__name { font-size: 19px; }

  .contact {
    position: absolute;
    right: 34px; top: 118px;
    text-align: right;
    font-family: "Montserrat", sans-serif;
    color: var(--ink);
  }
  .contact__name {
    font-family: "Amatic SC", cursive;
    font-weight: 700;
    font-size: 32px;
    line-height: 1;
    color: var(--brand-red);
  }
  .contact__role {
    font-size: 15px;
    font-weight: 500;
    margin-bottom: 14px;
  }
  .contact__line {
    font-size: 13px;
    line-height: 1.4;
  }

  .card--back .brand {
    position: absolute;
    left: 50%; top: 50%;
    transform: translate(-50%, -50%);
    gap: 16px;
  }
  .card--back .brand__dot { width: 86px; height: 86px; }
  .card--back .brand__name { font-size: 30px; white-space: nowrap; }
</style>
</head>
<body>
  <main class="stage">
    <section class="card card--front">
      <div class="footprint footprint--blue" role="img" aria-label="Blue child footprint illustration"></div>
      <div class="footprint footprint--orange" role="img" aria-label="Orange child footprint illustration"></div>

      <div class="brand">
        <span class="brand__dot"></span>
        <span class="brand__name">Bright Path Therapies</span>
      </div>

      <div class="contact">
        <p class="contact__name">Lorem Ipsum</p>
        <p class="contact__role">manager</p>
        <p class="contact__line">012 555 0148</p>
        <p class="contact__line">info@brightpaththerapies.example</p>
        <p class="contact__line">www.brightpaththerapies.example</p>
      </div>
    </section>

    <section class="card card--back">
      <div class="brand">
        <span class="brand__dot"></span>
        <span class="brand__name">Bright Path Therapies</span>
      </div>
    </section>
  </main>
</body>
</html>
```